Web Design Project for a beach town business owner who supports new families with their babies.

I'm looking for a basic website with the following pages: home, about, services, FAQs, blog, and contact page. I have images and content ready to go.

Target Market(s)

Men and women between the ages of 22 and 42, growing families

Industry/Entity Type

Postpartum Doula

Coding

Number of Pages Required

5+ page

Font styles to use
Serif
Other font styles liked:
• My logo font is "Nexa Bold" - so coordinating fonts with that are ideal

Colors
00AB8E
00BBA5
67D7C9
C6EFE9
E9F9F6
EE7325
F08F49
F5BC92
FAE3D3
FDF4ED

Requirements
Must have
• Warm and professional vibe, multicultural images, aligned with my branding colors and font ("Nexa Bold"; COLORS: light blue hex: #2FCEC2 R: 47 G: 206 B: 194 dark blue hex: #007C7C R: 0 G: 124 B: 124 orange hex: #F77B4E R: 247 G: 123 B: 78), good SEO
Should not have
• Ultra feminine images, baby bottles, cutesy images.

```html
<!DOCTYPE html>
<html lang="en">
<head>
<meta charset="utf-8">
<title>Harborline Families Postpartum Care</title>
<link rel="stylesheet" href="https://fonts.googleapis.com/css2?family=Didact+Gothic&family=Questrial&display=swap">
<style>
:root{
  --teal-dark:#00AB8E;
  --teal:#00BBA5;
  --teal-light:#67D7C9;
  --teal-pale:#C6EFE9;
  --teal-mist:#E9F9F6;
  --orange:#EE7325;
  --orange-soft:#F08F49;
  --orange-pale:#FDF4ED;
  --ink:#1f2326;
  --body:#3a3d40;
  --white:#ffffff;
}
*{box-sizing:border-box;margin:0;padding:0}
html,body{width:1200px;height:2814px;overflow:hidden}
body{position:relative;background:var(--white);font-family:"Didact Gothic",sans-serif;color:var(--body)}
.abs{position:absolute}
.heading{font-family:"Questrial",sans-serif;color:var(--ink);text-transform:uppercase;font-weight:400}

/* header */
.site-header{left:0;top:0;width:1200px;height:62px;background:var(--white);z-index:3}
.brand{left:200px;top:-17px;width:156px;height:156px;background:var(--white);border-radius:50%;border-bottom:5px solid var(--teal-light);display:flex;align-items:center;justify-content:center;padding-top:16px;z-index:4}
.brand-name{font-family:"Questrial",sans-serif;color:var(--teal-dark);font-size:15px;line-height:1.15;text-align:center}
.nav{left:428px;top:25px;display:flex;align-items:center;font-family:"Questrial",sans-serif;font-size:10.5px;color:var(--ink);z-index:4}
.nav a{color:inherit;text-decoration:none}
.nav .active{color:var(--orange)}
.nav .dot{width:3px;height:3px;border-radius:50%;background:var(--ink);margin:0 17px}
.call-btn{left:863px;top:16px;width:137px;height:30px;border-radius:15px;background:var(--teal-dark);color:var(--white);font-family:"Questrial",sans-serif;font-size:10.5px;display:flex;align-items:center;padding-left:6px;z-index:4}
.call-btn .ico{width:20px;height:20px;border-radius:50%;background:var(--white);display:flex;align-items:center;justify-content:center;margin-right:8px}

/* hero */
.hero{left:0;top:62px;width:1200px;height:563px;background:linear-gradient(160deg,#5e7a3c 0%,#4d6a30 40%,#3f6a52 70%,#1d8fb4 100%)}
.hero-title{left:200px;top:266px;width:440px;font-family:"Questrial",sans-serif;font-size:25.5px;line-height:30px;color:var(--white);font-weight:400}
.btn{display:flex;align-items:center;justify-content:space-between;border-radius:16px;color:var(--white);font-family:"Questrial",sans-serif;font-size:10px;text-transform:uppercase;padding:0 4px 0 14px;letter-spacing:.3px;text-decoration:none}
.btn .arrow{width:22px;height:22px;border-radius:50%;background:var(--white);display:flex;align-items:center;justify-content:center}
.btn-orange{background:var(--orange)}
.btn-teal{background:var(--teal-dark)}

/* intro */
.intro-title{left:200px;top:680px;width:820px;font-size:19.5px;line-height:22.5px;letter-spacing:.2px}
.intro p{font-size:10.8px;line-height:15px}
.intro-lead{left:200px;top:770px;width:800px}
.intro-lead p+p{margin-top:15px}
.intro-sub{left:200px;top:889px;width:720px;font-size:11.2px;line-height:15px;font-family:"Questrial",sans-serif;color:var(--ink)}
.support-list{left:200px;top:965px;width:535px;list-style:none;font-size:11.8px;line-height:15px;color:var(--ink)}
.support-list li{position:relative;padding-left:22px;margin-bottom:8px}
.support-list svg{position:absolute;left:0;top:2px}
.family-photo{left:794px;top:934px;width:206px;height:206px;background:linear-gradient(135deg,#d9d4cc,#7d6c60 55%,#3a3432)}
.intro-close{left:200px;top:1168px;width:800px}
.intro-close p+p{margin-top:15px}
.intro-close b{color:var(--ink);font-weight:400;font-family:"Questrial",sans-serif}

/* care links */
.care{left:0;top:1353px;width:1200px;height:351px;background:var(--teal-mist)}
.care-title{left:0;top:1420px;width:1200px;text-align:center;font-size:26px}
.care-card{top:1469px;width:274px;height:168px;display:flex;flex-direction:column;align-items:center;padding-top:31px}
.care-card .ring{width:76px;height:76px;border-radius:50%;border:1.5px dashed var(--orange-soft);display:flex;align-items:center;justify-content:center}
.care-card .label{margin-top:18px;font-family:"Questrial",sans-serif;font-size:16px;color:var(--ink);text-transform:uppercase}
.care-card.featured{background:var(--orange)}
.care-card.featured .ring{background:var(--white);border:none}
.care-card.featured .label{color:var(--white)}

/* blogs */
.blogs-title{left:0;top:1758px;width:1200px;text-align:center;font-size:26px}
.post{top:1813px;width:250px;height:292px;background:var(--white);box-shadow:0 0 0 1px #eef1f0;border-bottom:3px solid var(--teal-light)}
.post.current{border-bottom-color:var(--teal-dark)}
.post-img{width:250px;height:157px}
.post-body{padding:22px 25px 0}
.post-date{font-size:10px;color:var(--teal-dark);letter-spacing:.5px}
.post-title{margin-top:9px;font-size:12.5px;line-height:19px;color:var(--ink)}
.read-more{margin-top:20px;display:flex;align-items:center;font-family:"Questrial",sans-serif;font-size:10.5px;color:var(--teal-dark)}
.read-more .chev{margin-left:12px;width:28px;height:28px;border-radius:50%;display:flex;align-items:center;justify-content:center}
.post.current .chev{background:var(--teal-dark)}

/* contact */
.contact{left:0;top:2231px;width:1200px;height:550px;background:var(--teal-dark)}
.contact-title{left:0;top:2293px;width:1200px;text-align:center;font-size:26px;color:var(--white)}
.contact-sub{left:280px;top:2331px;width:640px;text-align:center;font-size:12.5px;line-height:19px;color:var(--white)}
.field{height:31px;border-radius:16px;background:var(--white);font-size:9.5px;color:#6b6f71;display:flex;align-items:center;justify-content:space-between;padding:0 16px}
.radio-q{font-size:9px;color:var(--white);display:flex;align-items:center;gap:7px}
.radio-q .opt{display:flex;align-items:center;gap:3px;margin-left:12px}
.radio-q .r{width:7px;height:7px;border:1px solid var(--white);border-radius:50%;display:inline-flex;align-items:center;justify-content:center}
.radio-q .r.on::after{content:"";width:3px;height:3px;border-radius:50%;background:var(--white)}
.message{left:294px;top:2610px;width:612px;height:93px;border-radius:14px;background:var(--white)}

.footer{left:0;top:2781px;width:1200px;height:33px;background:var(--orange);color:var(--white);font-size:9px;display:flex;align-items:center;justify-content:center;letter-spacing:.3px}
</style>
</head>
<body>

<header class="abs site-header"></header>
<div class="abs brand"><span class="brand-name">Harborline<br>Families</span></div>
<nav class="abs nav">
  <a class="active">HOME</a><span class="dot"></span>
  <a>ABOUT US</a><span class="dot"></span>
  <a>OUR SERCVICES</a><span class="dot"></span>
  <a>FAQS</a><span class="dot"></span>
  <a>CONTACT US</a>
</nav>
<div class="abs call-btn"><span class="ico"><svg width="11" height="11" viewBox="0 0 24 24"><path d="M6.6 10.8a15 15 0 0 0 6.6 6.6l2.2-2.2c.3-.3.7-.4 1-.2 1.1.4 2.3.6 3.6.6.6 0 1 .4 1 1V20c0 .6-.4 1-1 1A17 17 0 0 1 3 4c0-.6.4-1 1-1h3.5c.6 0 1 .4 1 1 0 1.2.2 2.4.6 3.6.1.3 0 .7-.2 1z" fill="#00AB8E"/></svg></span>Call - 555 0142 830</div>

<section class="abs hero" role="img" aria-label="Portrait photo of the postpartum doula outdoors in front of soft green foliage"></section>
<h1 class="abs hero-title">Congratulations on your<br>birth and welcome to Harborline<br>Families Postpartum Care</h1>
<a class="abs btn btn-orange" style="left:200px;top:382px;width:118px;height:31px">Contact us <span class="arrow"><svg width="11" height="11" viewBox="0 0 12 12"><path d="M2 6h8M7 3l3 3-3 3" stroke="#EE7325" stroke-width="1.4" fill="none"/></svg></span></a>

<section class="intro">
  <h2 class="abs heading intro-title">Hi, I'm Dana Reyes, a certified postpartum care expert and<br>educator serving families of all varieties in the greater San Diego<br>area and beyond</h2>
  <div class="abs intro-lead">
    <p>My passion as a professional is showing new parents just like you that whether you've just had your first child or your fifth, you can not only survive your postpartum period (also known as the 4th trimester), but you and your family can THRIVE – with the kind of compassionate, skilled, and targeted support for your unique needs that only an expert can provide. That's where I come in.</p>
    <p>Did you know that, on average, new parents won't see their midwife or obstetrician until 6 weeks after giving birth to their baby(ies)? Working with a postpartum care expert (also known as a doula) can help fill in this gap in continuity of care by providing individualized support for parents and families as they transition to life with their new baby.</p>
  </div>
  <p class="abs intro-sub">MY WORK INCLUDES FOUR KEY AREAS OF SUPPORT THAT ARE DESIGNED TO POSITIVELY IMPACT YOUR POSTPARTUM<br>PERIOD WITH YOUR BABY</p>
  <ul class="abs support-list">
    <li><svg width="10" height="10" viewBox="0 0 10 10"><circle cx="5" cy="5" r="4.4" stroke="#00AB8E" fill="none"/><path d="M3 5.1l1.4 1.4L7 3.8" stroke="#00AB8E" fill="none"/></svg>I enhance bonding and attachment between parents(s) and baby in the areas of feeding,<br>soothing, learning baby's cues, babywearing, and playing with baby</li>
    <li><svg width="10" height="10" viewBox="0 0 10 10"><circle cx="5" cy="5" r="4.4" stroke="#00AB8E" fill="none"/><path d="M3 5.1l1.4 1.4L7 3.8" stroke="#00AB8E" fill="none"/></svg>I provide practical, evidence-based information about baby care and help identify<br>what is normal and what is outside the range of normal for parent(s) and baby</li>
    <li><svg width="10" height="10" viewBox="0 0 10 10"><circle cx="5" cy="5" r="4.4" stroke="#00AB8E" fill="none"/><path d="M3 5.1l1.4 1.4L7 3.8" stroke="#00AB8E" fill="none"/></svg>I prioritize the mental and emotional health of parent(s) and help identify potential<br>warning signs that indicate that medical care may be needed</li>
    <li><svg width="10" height="10" viewBox="0 0 10 10"><circle cx="5" cy="5" r="4.4" stroke="#00AB8E" fill="none"/><path d="M3 5.1l1.4 1.4L7 3.8" stroke="#00AB8E" fill="none"/></svg>I offer hands-on support with baby(ies), older siblings, pets, and light home upkeep and<br>meal preparation</li>
  </ul>
  <div class="abs family-photo" role="img" aria-label="Photo of the doula seated on a sofa with a young couple holding their newborn"></div>
  <div class="abs intro-close">
    <p>Families who work with me report feeling more connected, happy, and informed than their parenting-veteran friends and family members – both during the<br>time that I work with them and beyond.</p>
    <p>Struggle is a normal part of growth and learning. Your postpartum period is a time for <b>healing and recovering from birth, bonding with your baby,<br>and establishing a healthy feeding relationship in whatever way works best for your family.</b> Let me show you how to remove the struggle<br>from this magical time!</p>
  </div>
  <a class="abs btn btn-teal" style="left:200px;top:1279px;width:156px;height:30px;padding-left:20px">Let's get started <span class="arrow"><svg width="11" height="11" viewBox="0 0 12 12"><path d="M2 6h8M7 3l3 3-3 3" stroke="#00AB8E" stroke-width="1.4" fill="none"/></svg></span></a>
</section>

<section class="abs care"></section>
<h2 class="abs heading care-title">Harborline Families Postpartum Care</h2>
<div class="abs care-card" style="left:188px">
  <div class="ring"><svg width="38" height="42" viewBox="0 0 38 42"><circle cx="19" cy="12" r="10" fill="#EE7325"/><path d="M1 41c0-11 8-17 18-17s18 6 18 17z" fill="#EE7325"/></svg></div>
  <span class="label">About us</span>
</div>
<div class="abs care-card featured" style="left:463px">
  <div class="ring"><svg width="34" height="40" viewBox="0 0 34 40"><circle cx="18" cy="8" r="6" fill="#EE7325"/><rect x="10" y="16" width="14" height="22" rx="5" fill="#EE7325"/><circle cx="14" cy="26" r="5" fill="#fff"/></svg></div>
  <span class="label">Our sercvices</span>
</div>
<div class="abs care-card" style="left:738px">
  <div class="ring"><svg width="42" height="38" viewBox="0 0 42 38"><rect x="2" y="2" width="18" height="14" rx="2" fill="#EE7325"/><rect x="20" y="12" width="18" height="14" rx="2" fill="#EE7325"/><rect x="2" y="22" width="16" height="13" rx="2" fill="#EE7325"/></svg></div>
  <span class="label">FAQs</span>
</div>

<h2 class="abs heading blogs-title">Latest blogs</h2>
<article class="abs post current" style="left:200px">
  <div class="post-img" role="img" aria-label="Photo of the doula holding two sleeping newborns" style="background:linear-gradient(135deg,#cfc7bd,#8b7466 60%,#4f6f8a)"></div>
  <div class="post-body">
    <div class="post-date">JULY-12-2021</div>
    <div class="post-title">There are many variations lorem Ipsum available, literature</div>
    <div class="read-more">READ MORE <span class="chev"><svg width="8" height="8" viewBox="0 0 8 8"><path d="M3 1l3 3-3 3" stroke="#fff" fill="none"/></svg></span></div>
  </div>
</article>
<article class="abs post" style="left:475px">
  <div class="post-img" role="img" aria-label="Photo of two mothers and a young child sitting by a tree in a park" style="background:linear-gradient(135deg,#9bbf6a,#5d7d3c 55%,#3a3328)"></div>
  <div class="post-body">
    <div class="post-date">JULY-12-2021</div>
    <div class="post-title">There are many variations lorem Ipsum available, literature</div>
    <div class="read-more">READ MORE <span class="chev"><svg width="8" height="8" viewBox="0 0 8 8"><path d="M3 1l3 3-3 3" stroke="#00AB8E" fill="none"/></svg></span></div>
  </div>
</article>
<article class="abs post" style="left:750px">
  <div class="post-img" role="img" aria-label="Black and white photo of parents cradling their newborn" style="background:linear-gradient(135deg,#e0e0e0,#6a6a6a 55%,#1c1c1c)"></div>
  <div class="post-body">
    <div class="post-date">JULY-12-2021</div>
    <div class="post-title">There are many variations lorem Ipsum available, literature</div>
    <div class="read-more">READ MORE <span class="chev"><svg width="8" height="8" viewBox="0 0 8 8"><path d="M3 1l3 3-3 3" stroke="#00AB8E" fill="none"/></svg></span></div>
  </div>
</article>
<a class="abs btn btn-teal" style="left:528px;top:2138px;width:144px;height:31px;padding-left:20px">View all blogs <span class="arrow"><svg width="11" height="11" viewBox="0 0 12 12"><path d="M2 6h8M7 3l3 3-3 3" stroke="#00AB8E" stroke-width="1.4" fill="none"/></svg></span></a>

<section class="abs contact"></section>
<h2 class="abs heading contact-title">Contact us</h2>
<p class="abs contact-sub">Your anchor is just a message away! Contact me today to schedule a no-pressure, free consultation<br>to see if we're a good fit for your needs</p>
<div class="abs field" style="left:294px;top:2395px;width:298px">Name</div>
<div class="abs field" style="left:607px;top:2395px;width:299px">Email</div>
<div class="abs field" style="left:294px;top:2440px;width:298px">Phone</div>
<div class="abs radio-q" style="left:624px;top:2450px">Have you had your baby(ies), yet? <span class="opt"><span class="r"></span>Yes</span><span class="opt"><span class="r on"></span>No</span></div>
<div class="abs field" style="left:294px;top:2487px;width:298px">If so, did you have a birth? <svg width="10" height="6" viewBox="0 0 10 6"><path d="M1 1l4 4 4-4" stroke="#00AB8E" fill="none"/></svg></div>
<div class="abs field" style="left:607px;top:2487px;width:299px">If not, what is your EDD? <svg width="9" height="9" viewBox="0 0 9 9"><rect x=".5" y="1.5" width="8" height="7" stroke="#00AB8E" fill="none"/><path d="M.5 3.5h8" stroke="#00AB8E"/></svg></div>
<div class="abs radio-q" style="left:310px;top:2535px">Is this your first baby? <span class="opt"><span class="r"></span>Yes</span><span class="opt"><span class="r on"></span>No</span></div>
<div class="abs field" style="left:294px;top:2563px;width:298px">If not, what are the ages of your older children?</div>
<div class="abs field" style="left:607px;top:2563px;width:299px">Are you interested in? <svg width="10" height="6" viewBox="0 0 10 6"><path d="M1 1l4 4 4-4" stroke="#00AB8E" fill="none"/></svg></div>
<div class="abs message"></div>
<a class="abs btn btn-orange" style="left:550px;top:2687px;width:100px;height:31px;padding-left:24px">Submit <span class="arrow"><svg width="11" height="11" viewBox="0 0 12 12"><path d="M2 6h8M7 3l3 3-3 3" stroke="#EE7325" stroke-width="1.4" fill="none"/></svg></span></a>

<footer class="abs footer">© 2021 HARBORLINE FAMILIES POSTPARTUM CARE. All Rights Reserved</footer>

</body>
</html>
```